Kickass billboard for motorway

Fix my old hauler - clue is in the name.
We have a 45ft billboard we're looking to design constructed from an old trailer we own (so we can be as creative as possible).
We provide a van buying service, being one of the only companies in the UK with the facilities to recover faulty, damaged and broken vans - from small car derived vans to large trucks and lorries.
ur niche in the market is different to car buying services, as buying and selling cars is often an emotionally driven process, whereas people often see and treat vans purely as a tool. There are alternatives to a car, public transport etc, but not to a work van - so people go out straight away and replace them immediately, often leaving the old broken van to sit on their drive or in their unit.
Looking to start building a brand asset bank.
Feel free to check out our website to get a feel for what we do:
Fixmyoldhauler.co.uk

Target Market(s)

Van owners/drivers & fleet managers

Industry/Entity Type

Automotive

Font styles to use
Sans Serif

Colors
34a7d8

Requirements
Must have
• Eye-catching - very eye-catching.
We want to advertise the fact we collect vehicles for free.
We pay instantly upon arrival.
Our phone number 0161 493 7062
Our website www.fixmyoldhauler.co.uk
Nice to have
• 3d elements - we have the ability to get 3d props for the billboard including damaged vans etc.

```html
<!DOCTYPE html>
<html lang="en">
<head>
<meta charset="utf-8">
<title>Fix my old hauler – Motorway Billboard</title>
<link rel="stylesheet" href="https://fonts.googleapis.com/css2?family=Roboto+Condensed:wght@700;800;900&display=swap">
<style>
  :root {
    --red: #ed1c24;
    --navy: #1c1f6c;
    --ink: #111111;
    --white: #ffffff;
    --stage: #e9ecef;
    --photo-sky: #e8d9b8;
    --photo-trees: #5d6b3a;
    --photo-road: #8d8f8c;
  }
  * { box-sizing: border-box; margin: 0; padding: 0; }
  html, body {
    width: 1200px;
    height: 1200px;
    overflow: hidden;
    background: var(--stage);
    font-family: "Roboto Condensed", "Arial Narrow", sans-serif;
  }
  .billboard {
    position: absolute;
    left: 40px;
    top: 400px;
    width: 1120px;
    height: 400px;
    background: var(--white);
    overflow: hidden;
    box-shadow: 0 10px 30px rgba(0,0,0,0.18);
  }
  .billboard__shapes {
    position: absolute;
    inset: 0;
    width: 1120px;
    height: 400px;
  }
  .headline {
    position: absolute;
    font-weight: 900;
    text-transform: uppercase;
    line-height: 1;
    letter-spacing: -0.5px;
    white-space: nowrap;
  }
  .headline--collect { left: 556px; top: 26px;  font-size: 52px; color: var(--ink); }
  .headline--paid    { left: 556px; top: 166px; font-size: 54px; color: var(--ink); }
  .headline--arrival { left: 616px; top: 222px; font-size: 54px; color: var(--navy); }
  .accent-navy { color: var(--navy); }
  .accent-red  { color: var(--red); }
  .free-tag {
    position: absolute;
    left: 724px;
    top: 88px;
    padding: 6px 16px 4px;
    background: var(--red);
    color: var(--white);
    font-weight: 900;
    font-size: 54px;
    line-height: 1;
    text-transform: uppercase;
    white-space: nowrap;
    box-shadow: 6px 6px 0 rgba(0,0,0,0.18);
  }
  .contact-phone {
    position: absolute;
    left: 24px;
    top: 321px;
    display: flex;
    align-items: center;
    gap: 10px;
    color: var(--white);
    font-weight: 700;
    font-size: 52px;
    line-height: 1;
    white-space: nowrap;
  }
  .contact-phone svg { width: 36px; height: 36px; flex: none; }
  .contact-web {
    position: absolute;
    left: 476px;
    top: 324px;
    width: 630px;
    text-align: center;
    color: var(--white);
    font-weight: 700;
    font-size: 48px;
    line-height: 1;
    white-space: nowrap;
  }
</style>
</head>
<body>
  <main class="billboard">
    <svg class="billboard__shapes" viewBox="0 0 1120 400">
      <defs>
        <linearGradient id="photoTone" x1="0" y1="0" x2="0" y2="1">
          <stop offset="0" stop-color="var(--photo-sky)"/>
          <stop offset="0.45" stop-color="var(--photo-trees)"/>
          <stop offset="1" stop-color="var(--photo-road)"/>
        </linearGradient>
      </defs>
      <polygon class="hero-photo" role="img"
               aria-label="Photo of a white panel van driving along a tree-lined country road"
               points="0,0 484,0 428,296 0,296" fill="url(#photoTone)"/>
      <polygon class="band band--navy" points="460,296 1120,296 1120,400 440,400" fill="var(--navy)"/>
      <polygon class="band band--red" points="484,0 516,0 440,400 0,400 0,296 428,296" fill="var(--red)"/>
    </svg>

    <h1 class="headline headline--collect">We collect <span class="accent-navy">vehicles</span></h1>
    <div class="free-tag">For free</div>
    <h2 class="headline headline--paid">Get paid <span class="accent-red">instantly</span></h2>
    <h2 class="headline headline--arrival">Upon arrival</h2>

    <div class="contact-phone">
      <svg viewBox="0 0 40 40" aria-hidden="true">
        <circle cx="20" cy="20" r="17" fill="none" stroke="var(--white)" stroke-width="3"/>
        <path d="M13 11c1-1 3-1 4 0l2 3c1 1 0 2-1 3l-1 1c1 3 3 5 6 6l1-1c1-1 2-2 3-1l3 2c1 1 1 3 0 4l-2 2c-6 0-16-10-16-16z" fill="var(--white)"/>
      </svg>
      <span>0161 493 7062</span>
    </div>
    <div class="contact-web">www.fixmyoldhauler.co.uk</div>
  </main>
</body>
</html>
```